Company or website name
- Brivolt
- Links to the website
- http://brivolt.tarnquistsites.example/
- Describe your company and organization and target audience
- We sell cleaning chemicals to service companies.
- The design should have the following
- We want to have a header image in place of the sliding photo on the home page that shows the products laid out nicely with the logo.
- Other Facts

```html
<!DOCTYPE html>
<html lang="en">
<head>
<meta charset="utf-8">
<title>Brivolt – Header Banner</title>
<link rel="stylesheet" href="https://fonts.googleapis.com/css2?family=Montserrat:wght@800&family=Arimo:wght@700&family=Lato:wght@700&display=swap">
<style>
  :root {
    --stage: #2f2f2f;
    --ink: #111111;
    --lime: #a3e505;
    --leaf: #8cc63f;
    --field-green: #4caf3e;
    --sky: #3ea3dc;
    --sky-light: #7cc8f0;
    --rim: #e4e4e4;
    --paper: #ffffff;
  }
  html, body {
    margin: 0;
    width: 1200px;
    height: 1200px;
    overflow: hidden;
    background: var(--stage);
  }
  .banner {
    position: absolute;
    left: 66px;
    top: 177px;
    width: 1070px;
    height: 850px;
    overflow: hidden;
    background: var(--paper);
  }
  .banner__art {
    position: absolute;
    inset: 0;
    width: 1070px;
    height: 850px;
  }
  .brand {
    position: absolute;
    left: 154px;
    top: 66px;
    display: flex;
    align-items: center;
    gap: 18px;
  }
  .brand__name {
    font-family: "Montserrat", sans-serif;
    font-weight: 800;
    font-size: 110px;
    line-height: 1;
    letter-spacing: -4px;
    color: var(--ink);
  }
  .brand__dot {
    width: 120px;
    height: 120px;
    border-radius: 50%;
    background: var(--leaf);
  }
  .tagline {
    position: absolute;
    left: 154px;
    top: 224px;
    margin: 0;
    font-family: "Arimo", sans-serif;
    font-weight: 700;
    font-size: 24px;
    color: var(--ink);
  }
  .web-address {
    position: absolute;
    left: 624px;
    top: 802px;
    margin: 0;
    font-family: "Lato", sans-serif;
    font-weight: 700;
    font-size: 19px;
    letter-spacing: 6.5px;
    color: var(--ink);
  }
</style>
</head>
<body>
<main class="banner">
  <svg class="banner__art" viewBox="82 221 1338 1062" xmlns="http://www.w3.org/2000/svg">
    <defs>
      <linearGradient id="foliage-wash" x1="0" y1="0" x2="0" y2="1">
        <stop offset="0" stop-color="#dfeed6"/>
        <stop offset="0.45" stop-color="#f6faf3"/>
        <stop offset="1" stop-color="#ffffff"/>
      </linearGradient>
      <linearGradient id="blue-ring" x1="0" y1="0" x2="0" y2="1">
        <stop offset="0" stop-color="var(--sky)"/>
        <stop offset="1" stop-color="var(--sky-light)"/>
      </linearGradient>
      <radialGradient id="showroom" cx="0.5" cy="0.25" r="0.8">
        <stop offset="0" stop-color="#d6d6d6"/>
        <stop offset="0.6" stop-color="#f4f4f4"/>
        <stop offset="1" stop-color="#ffffff"/>
      </radialGradient>
      <radialGradient id="leaf-glow" cx="0.5" cy="0.5" r="0.5">
        <stop offset="0" stop-color="#a6d83a"/>
        <stop offset="0.7" stop-color="#cde79a"/>
        <stop offset="1" stop-color="#ffffff" stop-opacity="0"/>
      </radialGradient>
      <linearGradient id="buckets" x1="0" y1="0" x2="0" y2="1">
        <stop offset="0" stop-color="#f2f2f2"/>
        <stop offset="0.55" stop-color="#e2ec9a"/>
        <stop offset="1" stop-color="#f7f7f7"/>
      </linearGradient>
    </defs>

    <rect class="backdrop" x="82" y="221" width="1338" height="1062" fill="url(#foliage-wash)" role="img" aria-label="Soft blurred foliage backdrop"/>

    <ellipse class="leaf-sprig" cx="420" cy="760" rx="150" ry="165" fill="url(#leaf-glow)" role="img" aria-label="Pair of green leaves"/>

    <circle class="field-rim" cx="380" cy="1750" r="785" fill="var(--rim)"/>
    <circle class="field" cx="380" cy="1750" r="752" fill="var(--field-green)"/>

    <circle class="lime-outline" cx="1260" cy="1013" r="528" fill="var(--ink)"/>
    <circle class="lime-arc" cx="1260" cy="1013" r="512" fill="var(--lime)"/>

    <circle class="ring-gap" cx="1050" cy="1171" r="590" fill="var(--paper)"/>
    <circle class="ring-blue" cx="1050" cy="1171" r="576" fill="url(#blue-ring)"/>
    <circle class="ring-white" cx="1050" cy="1171" r="543" fill="var(--paper)"/>
    <circle class="ring-black" cx="1050" cy="1171" r="512" fill="var(--ink)"/>
    <circle class="showroom" cx="1050" cy="1171" r="484" fill="url(#showroom)"/>

    <rect class="product-lineup" x="655" y="810" width="695" height="420" rx="30" fill="url(#buckets)" role="img" aria-label="Range of Brivolt cleaning chemical buckets arranged in a group"/>
  </svg>

  <div class="brand">
    <span class="brand__name">Brivolt</span>
    <span class="brand__dot"></span>
  </div>
  <p class="tagline">We sell cleaning chemicals to service companies</p>
  <p class="web-address">www.mywebsite.com</p>
</main>
</body>
</html>
```